NEED VIBRANT DIGTAL MENUS

NEED A NEW DESIGN FOR MENU SCREENS

SEE ATTACHED FOR EXISTING MENUS

Requirements
Must have
• FLOW. COLOR. ORGANIZATION. SOPHISTICATION.
Nice to have
• INCORPORATE LOGO IN DESIGNS

```html
<!DOCTYPE html>
<html lang="en">
<head>
<meta charset="UTF-8">
<title>Corvelli Menu Board</title>
<link href="https://fonts.googleapis.com/css2?family=Alfa+Slab+One&family=Fira+Sans+Extra+Condensed:wght@400;500;600;700&family=Zilla+Slab:wght@700&display=swap" rel="stylesheet">
<style>
:root{
  --stage:#141414;
  --board:#f1e8d8;
  --card:#f6f3ee;
  --navy:#1b3d55;
  --red:#b5371b;
  --ink:#1a1a1a;
  --white:#ffffff;
  --cream:#fbf6ee;
}
*{margin:0;padding:0;box-sizing:border-box}
html,body{width:770px;height:1200px;overflow:hidden;background:var(--stage)}
.stage{position:relative;width:770px;height:1200px;background:var(--stage);font-family:"Fira Sans Extra Condensed",sans-serif;color:var(--navy)}
.board{position:absolute;left:84px;top:65px;width:602px;height:1071px;background:var(--board)}
.abs{position:absolute}
.brand{position:absolute;left:0;top:78px;width:770px;text-align:center;font-family:"Alfa Slab One",serif;font-size:36px;letter-spacing:1px;color:var(--navy);line-height:1}
.card{position:absolute;left:122px;width:529px;background:var(--card);border-radius:26px}
.tag{position:absolute;background:var(--red);color:var(--white);font-weight:700;display:flex;align-items:center;justify-content:center;border-radius:3px;letter-spacing:.3px}
.section-title{position:absolute;font-family:"Zilla Slab",serif;font-weight:700;line-height:1;text-align:center}
.hours{position:absolute;left:572px;top:154px;font-weight:700;font-size:13px;line-height:15px;color:var(--ink)}
.divider{position:absolute;left:557px;top:155px;width:1.5px;height:28px;background:var(--ink)}
.photo{position:absolute;border-radius:2px}
.oval{position:absolute;width:58px;height:28px;border-radius:50%;background:var(--navy);color:var(--white);font-weight:600;font-size:11px;display:flex;align-items:center;justify-content:center}
.price{position:absolute;background:var(--red);color:var(--white);font-weight:600;font-size:9.5px;border-radius:3px;display:flex;align-items:center;justify-content:center;height:17px}
.price.light{background:var(--cream);color:var(--navy)}
.label{position:absolute;text-align:center;font-weight:700;color:var(--navy);line-height:1.05;white-space:nowrap}
.note{position:absolute;text-align:center;font-size:5px;line-height:7px;color:#4a5560;text-transform:uppercase}
.frame{position:absolute;border:1.3px solid var(--red)}
.red-band{position:absolute;background:var(--red)}
.copy{position:absolute;font-size:9.5px;color:var(--ink);line-height:12.5px;font-weight:500}
.vert{position:absolute;left:397px;top:538px;width:26px;height:174px;background:var(--red);border-radius:5px;color:var(--white);font-weight:700;font-size:10.5px;display:flex;align-items:center;justify-content:center;writing-mode:vertical-rl;transform:rotate(180deg);letter-spacing:.3px}
.white{color:var(--white)}
</style>
</head>
<body>
<div class="stage">
  <div class="board"></div>
  <div class="brand">CORVELLI</div>

  <!-- Breakfast -->
  <div class="card" style="top:129px;height:334px"></div>
  <div class="tag" style="left:148px;top:148px;width:208px;height:35px;font-size:15.5px">BACON, EGG &amp; CHEESE</div>
  <div class="section-title" style="left:370px;top:146px;font-size:38px;color:var(--red)">Breakfast</div>
  <div class="divider"></div>
  <div class="hours">6:00 AM<br>10:00 AM</div>

  <div class="photo" role="img" aria-label="Bacon, egg and cheese on a sesame bagel" style="left:148px;top:200px;width:208px;height:102px;background:linear-gradient(160deg,#a8421a,#e0a14a 55%,#f2d27a)"></div>
  <div class="oval" style="left:222px;top:278px">$4.59</div>
  <div class="photo" role="img" aria-label="Ham, egg and cheese on a roll" style="left:372px;top:200px;width:117px;height:89px;background:linear-gradient(170deg,#9aa3ad,#d9a35f 45%,#f0d47a)"></div>
  <div class="oval" style="left:401px;top:268px">$4.59</div>
  <div class="label" style="left:372px;top:301px;width:117px;font-size:11px">HAM, EGG &amp; CHEESE</div>
  <div class="photo" role="img" aria-label="Bologna, egg and cheese on toast" style="left:505px;top:200px;width:117px;height:89px;background:linear-gradient(170deg,#ece8e2,#d4a768 50%,#c9826e)"></div>
  <div class="oval" style="left:539px;top:266px">$5.49</div>
  <div class="label" style="left:500px;top:301px;width:127px;font-size:11px">BOLOGNA,EGG &amp; CHEESE</div>

  <div class="photo" role="img" aria-label="Sausage, egg and cheese on an english muffin" style="left:148px;top:329px;width:208px;height:92px;background:linear-gradient(170deg,#5a4a3e,#d49a58 40%,#e6a33a)"></div>
  <div class="oval" style="left:222px;top:407px">$5.99</div>
  <div class="label" style="left:148px;top:441px;width:208px;font-size:11px">SAUSAGE, EGG &amp; CHEESE</div>
  <div class="photo" role="img" aria-label="Fried chicken, egg and cheese biscuit" style="left:372px;top:329px;width:117px;height:92px;background:linear-gradient(170deg,#4d6a3a,#e6cfa0 35%,#d59a4a)"></div>
  <div class="oval" style="left:401px;top:408px">$6.99</div>
  <div class="label" style="left:366px;top:441px;width:129px;font-size:11px">CHICKEN, EGG &amp; CHEESE</div>
  <div class="photo" role="img" aria-label="Steak, egg and cheese burger with fries" style="left:505px;top:329px;width:117px;height:92px;background:linear-gradient(170deg,#2f5a2a,#a06238 45%,#e2b35c)"></div>
  <div class="oval" style="left:539px;top:408px">$7.99</div>
  <div class="label" style="left:505px;top:441px;width:117px;font-size:11px">STEAK EGG &amp; CHEESE</div>

  <!-- Lunch: burgers and subs -->
  <div class="card" style="top:466px;height:332px"></div>
  <div class="frame" style="left:144px;top:490px;width:254px;height:294px;border-radius:8px 0 0 14px;border-right:none;border-top:none"></div>
  <div class="tag" style="left:148px;top:478px;width:164px;height:26px;font-size:12px">HANDCRAFTED BURGERS</div>
  <div class="section-title" style="left:320px;top:474px;width:134px;font-size:34px;color:var(--navy)">LUNCH</div>
  <div class="tag" style="left:458px;top:478px;width:164px;height:26px;font-size:12px">HANDCRAFTED BURGERS</div>
  <div class="copy" style="left:164px;top:513px;width:150px">ALL BURGERS ARE 100% HAND MADE PATTIES</div>

  <div class="photo" role="img" aria-label="Half pound super cheeseburger" style="left:165px;top:555px;width:78px;height:48px;background:linear-gradient(180deg,#fff,#c98a4a 30%,#5d3a22 60%,#7fa648)"></div>
  <div class="price" style="left:214px;top:588px;width:30px">$8.49</div>
  <div class="label" style="left:155px;top:611px;width:98px;font-size:6px">1/2LB SUPER CHEESEBURGER</div>
  <div class="photo" role="img" aria-label="Crispy chicken burger with lettuce and tomato" style="left:259px;top:530px;width:117px;height:70px;background:linear-gradient(180deg,#f4f1ec,#d99a4c 30%,#c9462f 50%,#e0a85a)"></div>
  <div class="price" style="left:344px;top:583px;width:34px">$6.49</div>
  <div class="label" style="left:250px;top:606px;width:135px;font-size:11.5px">1/4LB CHEESEBURGER</div>

  <div class="photo" role="img" aria-label="Quarter pound bacon cheeseburger" style="left:165px;top:629px;width:78px;height:49px;background:linear-gradient(180deg,#2a211c,#d08a44 35%,#9a3b26 60%,#6e4a30)"></div>
  <div class="price" style="left:214px;top:662px;width:30px">$7.49</div>
  <div class="label" style="left:155px;top:686px;width:98px;font-size:6px">1/4LB BACON CHEESEBURER</div>
  <div class="photo" role="img" aria-label="Bologna burger on a bun" style="left:259px;top:629px;width:117px;height:49px;background:linear-gradient(90deg,#1e1a17,#d8a66a 40%,#e9c89a 60%,#1e1a17)"></div>
  <div class="price" style="left:344px;top:661px;width:34px">$7.99</div>
  <div class="label" style="left:259px;top:686px;width:117px;font-size:10px">BOLOGNA BURGER</div>

  <div class="photo" role="img" aria-label="Half pound bacon super cheeseburger" style="left:165px;top:703px;width:78px;height:49px;background:linear-gradient(180deg,#fff,#d09048 30%,#f0b030 55%,#4a2e20)"></div>
  <div class="price" style="left:214px;top:736px;width:30px">$9.99</div>
  <div class="label" style="left:155px;top:760px;width:98px;font-size:6px;line-height:8px">1/2LB BACON SUPER<br>CHEESEBURGER</div>
  <div class="photo" role="img" aria-label="Super bologna burger" style="left:259px;top:703px;width:117px;height:49px;background:linear-gradient(160deg,#a02a1c,#d89a58 45%,#e8b040)"></div>
  <div class="price" style="left:344px;top:735px;width:34px">$9.99</div>
  <div class="label" style="left:259px;top:760px;width:117px;font-size:10px">SUPER BOLOGNA BURGER</div>

  <div class="copy" style="left:430px;top:514px;width:200px;text-align:center;font-weight:400">SERVED ON FRESH BAKED ROLLS</div>
  <div class="frame" style="left:410px;top:543px;width:220px;height:241px;border-radius:0 14px 0 0;border-left:none;border-bottom:none"></div>
  <div class="vert">HALF $11.99&nbsp;&nbsp;|&nbsp;&nbsp;WHOLE $17.99</div>

  <div class="photo" role="img" aria-label="Ham and cheese sub" style="left:445px;top:533px;width:60px;height:33px;border-radius:14px;background:linear-gradient(180deg,#d59650,#7fae52 55%,#e8c090)"></div>
  <div class="label" style="left:435px;top:570px;width:80px;font-size:9.5px">HAM &amp; CHEESE</div>
  <div class="photo" role="img" aria-label="Oven roasted chicken sub" style="left:538px;top:533px;width:55px;height:33px;border-radius:14px;background:linear-gradient(180deg,#d59650,#e7d8b8 55%,#8cb256)"></div>
  <div class="label" style="left:508px;top:571px;width:110px;font-size:9.5px">OVEN ROASTED CHICKEN</div>

  <div class="photo" role="img" aria-label="Italian sub" style="left:445px;top:585px;width:62px;height:35px;border-radius:14px;background:linear-gradient(180deg,#d59650,#c24a3a 55%,#e8c090)"></div>
  <div class="label" style="left:433px;top:626px;width:80px;font-size:9.5px">ITALIAN</div>
  <div class="note" style="left:433px;top:638px;width:80px">COOKED HAM, SALAMI &amp; PROVOLONE.</div>
  <div class="photo" role="img" aria-label="Combo sub" style="left:532px;top:585px;width:62px;height:35px;border-radius:14px;background:linear-gradient(180deg,#d59650,#b8594a 50%,#7aa24c)"></div>
  <div class="label" style="left:522px;top:626px;width:82px;font-size:9.5px">COMBO</div>
  <div class="note" style="left:516px;top:638px;width:94px">HAM, TURKEY &amp; ROAST BEEF</div>

  <div class="photo" role="img" aria-label="Cajun sub" style="left:447px;top:657px;width:58px;height:36px;border-radius:14px;background:linear-gradient(180deg,#d59650,#c0563e 50%,#e8c090)"></div>
  <div class="label" style="left:433px;top:698px;width:80px;font-size:9.5px">CAJUN</div>
  <div class="note" style="left:428px;top:710px;width:90px">HAM ,SMOKED TURKEY</div>
  <div class="photo" role="img" aria-label="Roast beef sub" style="left:532px;top:656px;width:66px;height:38px;border-radius:14px;background:linear-gradient(180deg,#e0a868,#7d3a30 50%,#eecfa6)"></div>
  <div class="label" style="left:524px;top:699px;width:82px;font-size:9.5px">ROAST BEEF</div>

  <div class="red-band" style="left:397px;top:723px;width:233px;height:61px;border-radius:0 0 2px 0"></div>
  <div class="label white" style="left:420px;top:733px;font-size:12.5px;text-align:left">STEAK CHEESE</div>
  <div class="label white" style="left:420px;top:751px;font-size:9.5px;text-align:left;font-weight:600">HALF<br>$12.99</div>
  <div class="abs" style="left:456px;top:752px;width:1.2px;height:22px;background:var(--white)"></div>
  <div class="label white" style="left:466px;top:751px;font-size:9.5px;text-align:left;font-weight:600">WHOLE<br>$21.99</div>
  <div class="photo" role="img" aria-label="Steak and cheese sub with peppers" style="left:508px;top:730px;width:100px;height:46px;border-radius:18px;background:linear-gradient(180deg,#e0a868,#f1ece2 45%,#c0402a 70%,#e0a868)"></div>

  <!-- Lunch: paninis and sandwiches -->
  <div class="card" style="top:800px;height:336px"></div>
  <div class="frame" style="left:144px;top:825px;width:254px;height:291px;border-radius:8px 0 0 14px;border-top:none"></div>
  <div class="tag" style="left:148px;top:810px;width:164px;height:26px;font-size:12px">FRESH GRILLED PANINIS</div>
  <div class="section-title" style="left:320px;top:806px;width:134px;font-size:34px;color:var(--red)">LUNCH</div>
  <div class="tag" style="left:458px;top:810px;width:164px;height:26px;font-size:12px">SANDWICHES</div>
  <div class="photo" role="img" aria-label="Bowl of potato chips" style="left:159px;top:835px;width:34px;height:20px;border-radius:0 0 14px 14px;background:linear-gradient(180deg,#f3d56a,#e3b43c)"></div>
  <div class="copy" style="left:195px;top:842px;font-weight:400">(SERVED WITH CHIPS) <b style="font-size:12.5px;font-weight:700;color:var(--navy)">$7.99</b></div>
  <div class="copy" style="left:476px;top:842px;font-weight:400">(SERVED WITH CHIPS)</div>
  <div class="photo" role="img" aria-label="Bowl of potato chips" style="left:572px;top:836px;width:34px;height:20px;border-radius:0 0 14px 14px;background:linear-gradient(180deg,#f3d56a,#e3b43c)"></div>

  <div class="frame" style="left:397px;top:863px;width:233px;height:253px;border-radius:0 8px 0 0;border-bottom:none"></div>

  <div class="photo" role="img" aria-label="Roast beef and cheddar panini" style="left:175px;top:866px;width:85px;height:48px;border-radius:10px;background:linear-gradient(150deg,#e4b468,#a8404a 45%,#e8b870)"></div>
  <div class="label" style="left:150px;top:920px;width:135px;font-size:8px">ROAST BEEF AND CHEDDAR</div>
  <div class="note" style="left:160px;top:931px;width:115px">HOME MADE ROAST BEEF SMOTHERED WITH CHEDDAR CHEESE</div>
  <div class="photo" role="img" aria-label="Steak and cheese panini" style="left:285px;top:865px;width:91px;height:50px;background:linear-gradient(150deg,#5a6a78,#d8a460 45%,#efe2c4)"></div>
  <div class="price" style="left:344px;top:899px;width:34px">$7.99</div>
  <div class="label" style="left:280px;top:920px;width:100px;font-size:8px">STEAK AND CHEESE</div>
  <div class="note" style="left:285px;top:931px;width:90px">HOT GRILLED STEAK SMOTHERED WITH CHEESE</div>

  <div class="photo" role="img" aria-label="Ham and swiss panini" style="left:170px;top:950px;width:90px;height:46px;border-radius:10px;background:linear-gradient(150deg,#e0a85a,#f1d890 45%,#e8a6a0 60%,#d99a50)"></div>
  <div class="label" style="left:160px;top:1006px;width:115px;font-size:8px">HAM AND SWISS</div>
  <div class="note" style="left:160px;top:1017px;width:115px">VIRGINIA BAKED HAM GRILLED WITH SWISS CHEESE TURKEY &amp; CHEESE</div>
  <div class="photo" role="img" aria-label="Corned beef and swiss panini" style="left:285px;top:950px;width:91px;height:50px;background:linear-gradient(150deg,#4a2a26,#c45a5a 45%,#d8b27a)"></div>
  <div class="label" style="left:275px;top:1006px;width:110px;font-size:8px">CORNED BEEF AND SWISS</div>
  <div class="note" style="left:285px;top:1017px;width:90px">HOT GRILLED STEAK SMOTHERED WITH CHEESE</div>

  <div class="photo" role="img" aria-label="Turkey and provolone panini" style="left:188px;top:1034px;width:56px;height:38px;border-radius:8px;background:linear-gradient(180deg,#d8a060,#7ba24c 40%,#d7a8a0 70%,#d8a060)"></div>
  <div class="label" style="left:150px;top:1078px;width:135px;font-size:8px">TURKEY AND PROVOLONE</div>
  <div class="note" style="left:160px;top:1089px;width:115px">SLICED TURKEY BREAST GRILLED WITH PROVOLONE CHEESE (PESTO OPTIONAL)</div>
  <div class="photo" role="img" aria-label="Buffalo chicken panini" style="left:286px;top:1034px;width:92px;height:40px;background:linear-gradient(150deg,#6e3a2a,#e2b46a 50%,#7ea650)"></div>
  <div class="label" style="left:280px;top:1078px;width:100px;font-size:8px">BUFFALO CHICKEN</div>
  <div class="note" style="left:280px;top:1089px;width:100px">GRILLED CHICKEN TOPPED WITH PROVOLONE CHEESE AND BUFFALO SAUCE</div>

  <div class="photo" role="img" aria-label="Turkey and cheese sandwich" style="left:418px;top:879px;width:70px;height:42px;border-radius:8px;background:linear-gradient(180deg,#b88250,#7ba24c 30%,#e8c88a 55%,#c04a36 75%,#b88250)"></div>
  <div class="price" style="left:476px;top:913px;width:34px">$7.99</div>
  <div class="label" style="left:416px;top:936px;width:80px;font-size:8.5px">TURKEY &amp; CHEESE</div>
  <div class="photo" role="img" aria-label="Country ham sandwich" style="left:530px;top:878px;width:70px;height:42px;border-radius:8px;background:linear-gradient(180deg,#d8a060,#e6b0b0 45%,#7ba24c)"></div>
  <div class="price" style="left:577px;top:913px;width:34px">$7.99</div>
  <div class="label" style="left:527px;top:934px;width:80px;font-size:8.5px">COUNTRY HAM</div>

  <div class="photo" role="img" aria-label="Ham and cheese sandwich" style="left:422px;top:955px;width:66px;height:46px;border-radius:8px;background:linear-gradient(180deg,#b88250,#5a9a3c 30%,#f0b030 55%,#e6a8a0 75%,#b88250)"></div>
  <div class="price" style="left:476px;top:990px;width:34px">$8.99</div>
  <div class="label" style="left:416px;top:1012px;width:80px;font-size:8.5px">HAM &amp; CHEESE</div>
  <div class="photo" role="img" aria-label="Bologna sandwich" style="left:535px;top:953px;width:64px;height:48px;border-radius:8px;background:linear-gradient(180deg,#d8a060,#d4787a 45%,#7ba24c 70%,#d8a060)"></div>
  <div class="price" style="left:577px;top:990px;width:34px">$7.99</div>
  <div class="label" style="left:527px;top:1012px;width:80px;font-size:8.5px">BOLOGNA</div>

  <div class="red-band" style="left:397px;top:1032px;width:233px;height:84px"></div>
  <div class="photo" role="img" aria-label="Roast beef sandwich" style="left:422px;top:1045px;width:78px;height:44px;border-radius:8px;background:linear-gradient(180deg,#c48a50,#7ba24c 30%,#8a4a3a 55%,#c48a50)"></div>
  <div class="price light" style="left:476px;top:1073px;width:34px">$5.99</div>
  <div class="label white" style="left:420px;top:1095px;width:80px;font-size:8px">ROAST BEEF</div>
  <div class="photo" role="img" aria-label="Club sandwich" style="left:533px;top:1043px;width:76px;height:46px;border-radius:8px;background:linear-gradient(180deg,#e0b060,#7ba24c 35%,#f1ece2 55%,#e0b060)"></div>
  <div class="price light" style="left:577px;top:1073px;width:34px">$8.99</div>
  <div class="label white" style="left:533px;top:1095px;width:80px;font-size:8px">CLUB</div>
</div>
</body>
</html>
```